Business cards, letterhead, envelopes for Business Brokerage Firm
Business cards, letterhead, envelopes, fax cover sheet, postcards
Business cards, letterhead, envelopes for Business Brokerage Firm -
Creative Brief
Professional
Marek Dunholt
President
438 North Ferris Lane, Suite #516 Lakeholm, Illinois 60199
marek@kelvrabusinessbrokers.com
www.kelvrabusinessbrokers.com
we do not have a slogan yet, if you have any ideas, feel free to add it in. We like the blues and grays for color.
We Sell Businesses -company sales or mergers -restaurant sales specialist -commercial real estate sales -exit/sale strategy consulting -operations consulting -estimates of value

```html
<!DOCTYPE html>
<html lang="en">
<head>
<meta charset="utf-8">
<title>Kelvra Meridian Partners – Stationery</title>
<link href="https://fonts.googleapis.com/css2?family=Cinzel:wght@500&family=Open+Sans:wght@400;600&display=swap" rel="stylesheet">
<style>
  :root {
    --backdrop: #e4e6e8;
    --paper: #ffffff;
    --ink: #4a5560;
    --ink-soft: #7d8790;
    --brand: #3d5566;
    --blue-deep: #0b2a3f;
    --blue-mid: #1d5878;
    --blue-light: #3f86a8;
    --faint: #eef0f2;
  }
  * { box-sizing: border-box; margin: 0; padding: 0; }
  html, body { width: 1200px; height: 734px; overflow: hidden; }
  body {
    background: var(--backdrop);
    font-family: "Open Sans", Arial, sans-serif;
    color: var(--ink);
    position: relative;
  }
  .sheet { position: absolute; background: var(--paper); box-shadow: 0 2px 8px rgba(0,0,0,.18); overflow: hidden; }

  /* brand lockup: invented name, one colour, one weight */
  .brand { display: flex; align-items: center; gap: 8px; }
  .brand-dot { width: 30px; height: 30px; border-radius: 50%; background: var(--blue-mid); flex: none; }
  .brand-name {
    font-family: "Cinzel", Georgia, serif; font-weight: 500; color: var(--brand);
    line-height: 1.15; letter-spacing: .5px;
  }
  .brand-name span { display: block; }

  .contact { font-size: 6px; line-height: 1.6; color: var(--ink-soft); }

  /* business card front */
  .card-front { left: 336px; top: 48px; width: 300px; height: 186px; }
  .card-front .edge { position: absolute; left: 0; top: 0; bottom: 0; width: 10px;
    background: linear-gradient(180deg, var(--blue-light), var(--blue-deep)); }
  .card-front .brand { position: absolute; left: 22px; top: 20px; }
  .card-front .brand-name { font-size: 12px; }
  .card-front .portrait { position: absolute; left: 198px; top: 18px; width: 30px; height: 38px;
    background: linear-gradient(180deg, #8a97a3, #3b4a57); }
  .card-front .person { position: absolute; left: 198px; top: 60px; font-size: 7px; color: var(--blue-mid); }
  .card-front .person small { display: block; color: var(--ink-soft); font-size: 6px; }
  .card-front .contact { position: absolute; left: 22px; bottom: 14px; }

  /* business card back */
  .card-back { left: 197px; top: 250px; width: 307px; height: 170px;
    background: radial-gradient(ellipse at 50% 35%, var(--blue-light), var(--blue-mid) 45%, var(--blue-deep)); color: #fff; }
  .card-back h2 { position: absolute; top: 10px; width: 100%; text-align: center; font-weight: 400; font-size: 10px; letter-spacing: .5px; }
  .card-back .mark { position: absolute; left: 139px; top: 30px; width: 28px; height: 28px; border-radius: 50%; background: rgba(255,255,255,.8); }
  .card-back ul { position: absolute; left: 102px; top: 70px; list-style: none; font-size: 7px; line-height: 1.6; }
  .card-back li::before { content: "\25A0"; font-size: 5px; margin-right: 5px; vertical-align: 1px; }

  /* envelope */
  .envelope { left: 156px; top: 444px; width: 473px; height: 276px; }
  .envelope .flap { position: absolute; left: 0; top: 0; width: 100%; height: 60px; }
  .envelope .brand { position: absolute; left: 22px; top: 74px; }
  .envelope .brand-name { font-size: 13px; }
  .envelope .return { position: absolute; left: 22px; top: 128px; }
  .envelope .contact-bottom { position: absolute; left: 22px; bottom: 14px; }
  .envelope .ghost { position: absolute; right: 18px; bottom: 10px; font-family: "Cinzel", Georgia, serif; font-weight: 500; font-size: 58px; color: var(--faint); }

  /* letterhead */
  .letterhead { left: 660px; top: 48px; width: 396px; height: 648px; }
  .letterhead .edge { position: absolute; left: 0; top: 0; bottom: 0; width: 14px;
    background: linear-gradient(180deg, var(--blue-light), var(--blue-deep) 70%, var(--blue-mid)); }
  .letterhead .brand { position: absolute; left: 28px; top: 22px; }
  .letterhead .brand-name { font-size: 16px; }
  .letterhead .brand-dot { width: 38px; height: 38px; }
  .letterhead .person { position: absolute; left: 238px; top: 26px; font-size: 8px; color: var(--blue-mid); }
  .letterhead .person small { display: block; color: var(--ink-soft); font-size: 7px; }
  .letterhead .contact { position: absolute; left: 28px; bottom: 22px; }
  .letterhead .ghost { position: absolute; right: 16px; bottom: 40px; font-family: "Cinzel", Georgia, serif; font-weight: 500; font-size: 72px; color: var(--faint); }
</style>
</head>
<body>

<section class="sheet card-front" aria-label="Business card front">
  <div class="edge"></div>
  <div class="brand"><div class="brand-dot"></div>
    <div class="brand-name"><span>Kelvra</span><span>Meridian</span><span>Partners</span></div></div>
  <div class="portrait" role="img" aria-label="Portrait photograph of the president"></div>
  <p class="person">Marek Dunholt<small>President</small></p>
  <p class="contact">438 North Ferris Lane, Suite #516<br>Lakeholm, Illinois 60199<br>Phone: 847-555-0142 | Fax: 847-555-0143<br>Email: marek@kelvrabusinessbrokers.com<br>Web: www.kelvrabusinessbrokers.com</p>
</section>

<section class="sheet card-back" aria-label="Business card back">
  <h2>We Sell Businesses</h2>
  <div class="mark"></div>
  <ul>
    <li>Company Sales or Mergers</li>
    <li>Restaurant Sales Specialist</li>
    <li>Commercial Real Estate Sales</li>
    <li>Exit/Sale Strategy Consulting</li>
    <li>Operations Consulting</li>
    <li>Estimates of Value</li>
  </ul>
</section>

<section class="sheet envelope" aria-label="Envelope">
  <svg class="flap" viewBox="0 0 473 60" preserveAspectRatio="none" aria-hidden="true">
    <defs><linearGradient id="flapBlue" x1="0" x2="1"><stop offset="0" stop-color="#0b2a3f"/><stop offset=".5" stop-color="#3f86a8"/><stop offset="1" stop-color="#0b2a3f"/></linearGradient></defs>
    <polygon points="0,0 473,0 473,14 236,58 0,14" fill="url(#flapBlue)"/>
  </svg>
  <div class="brand"><div class="brand-dot"></div>
    <div class="brand-name"><span>Kelvra</span><span>Meridian</span><span>Partners</span></div></div>
  <p class="contact return">438 North Ferris Lane, Suite #516<br>Lakeholm, Illinois 60199</p>
  <p class="contact contact-bottom">Phone: 847-555-0142 | Fax: 847-555-0143<br>Web: www.kelvrabusinessbrokers.com</p>
  <div class="ghost">Kelvra</div>
</section>

<section class="sheet letterhead" aria-label="Letterhead">
  <div class="edge"></div>
  <div class="brand"><div class="brand-dot"></div>
    <div class="brand-name"><span>Kelvra</span><span>Meridian</span><span>Partners</span></div></div>
  <p class="person">Marek Dunholt<small>President</small></p>
  <div class="ghost">Kelvra</div>
  <p class="contact">Phone: 847-555-0142 | Fax: 847-555-0143<br>438 North Ferris Lane, Suite #516, Lakeholm, Illinois 60199<br>Email: marek@kelvrabusinessbrokers.com<br>Web: www.kelvrabusinessbrokers.com</p>
</section>

</body>
</html>
```